Equipment financing with a focus on truck financing, need a business card

Looking to get a business card designed that stands out to represent my financing company. Vornel Truck & Equipment Financing. Even though I can finance all types of equipment my main focus will be on trucks. I can do financing all across Canada.I liked the design on the one I attached for Tessmark Holdings Corp.I want a truck picture to be on the card like the Brisko Lending card (this is not my company, it is someone elses and I've attached it as a sample) . If you can add a construction piece of equipment as well that would be great, something along the lines of the attachment for Brisko Lending. I want the Khanda symbol as well on the card, it can be one color if you choose, I thought something like the attachment stood out more. The Khanda is a symbol of Sikh faith. I am targeting most of my business to Sikh truck drivers. Card should have a black background so it stands out. It can be horizontal or vertical or a combination of both.Thinking the front of the card has a larger Khanda symbol and then a smaller one inside of it and then my name Vornel Truck & Equipment Financing .
Target Market(s)
Deal with people in all types of industries
Industry/Entity Type
Finance
Contact Information for Business Card
The front could be split black and other colors to make the khanda and lettering pop out. Open to any type of design.
Back of card would say
President
Derek Mowat
Mobile
403 555 0172
Email
Derek.Vornelli@quillbrookfunding.com
at the bottom like the Tessmark Holdings Corp card I want it to say and stand out
EQUIPMENT FINANCE SPECIALIST
am open to anything that looks great and stands out, modern and bold.
Colors
Designer to choose colors to be used in the design.
Requirements
Must have
- I would like the color of the khanda symbol to be similar to the picture I attached, kind of a goldish color, make the letters in a similar color as well
- - Modern
- - Different
- - Stand Out
- - Makes an Impression
Nice to have
- In summary, Brisko Lending is not my logo nor my business name its. I would like something similar though with a truck on the card, and if there is a way perhaps a piece of construction equipment.
- VORNEL TRUCK & EQUIPMENT FINANCING is the name of my company.
- I want a card that stands out and is bold like the Tessmark Holdings Corp card I attached
- The Khanda is a sikh symbol, I attached a pic of what it looks like.

```html
<!DOCTYPE html>
<html lang="en">
<head>
<meta charset="utf-8">
<title>Vornel Truck &amp; Equipment Financing – Business Card</title>
<link href="https://fonts.googleapis.com/css2?family=Oswald:wght@600&family=Roboto:wght@400&family=Montserrat:wght@700&display=swap" rel="stylesheet">
<style>
  :root{
    --page:#e9e4dc;
    --card-dark:#0b0b0c;
    --card-mid:#1d1d1f;
    --gold:#d9ad2c;
    --gold-light:#f3d45a;
    --gold-deep:#a77a12;
    --band-text:#1a1405;
    --contact:#e8c548;
  }
  *{margin:0;padding:0;box-sizing:border-box}
  html,body{width:900px;height:1200px;overflow:hidden;background:var(--page)}
  .canvas{position:relative;width:900px;height:1200px}
  .card{
    position:absolute;left:85px;width:735px;height:430px;border-radius:22px;overflow:hidden;
    background:
      repeating-linear-gradient(115deg,rgba(255,255,255,.025) 0 1px,transparent 1px 4px),
      linear-gradient(120deg,var(--card-dark) 0%,var(--card-mid) 45%,var(--card-dark) 100%);
    box-shadow:0 8px 18px rgba(0,0,0,.35);
  }
  .card--front{top:130px}
  .card--back{top:633px}
  .brand{position:absolute;text-align:center;color:var(--gold)}
  .brand__mark{display:block;margin:0 auto 22px;width:26px;height:26px;background:var(--gold)}
  .brand__name{font-family:'Oswald',sans-serif;font-weight:600;font-size:29px;letter-spacing:.3px;line-height:1;white-space:nowrap}
  .brand__sub{display:flex;align-items:center;justify-content:center;gap:12px;margin-top:8px;
    font-family:'Oswald',sans-serif;font-weight:600;font-size:17px;letter-spacing:1.5px;line-height:1}
  .brand__sub::before,.brand__sub::after{content:"";display:block;width:96px;height:1.5px;background:var(--gold)}
  .card--front .brand{left:55px;top:130px;width:330px}
  .card--back .brand{left:0;right:0;top:188px}
  .divider{position:absolute;left:55px;right:52px;top:296px;height:2px;background:var(--gold)}
  .person{position:absolute;left:55px;top:310px;color:var(--gold)}
  .person__name{font-family:'Oswald',sans-serif;font-weight:600;font-size:22px;line-height:1.15}
  .person__title{font-family:'Montserrat',sans-serif;font-weight:700;font-size:15px;letter-spacing:.5px}
  .contact{position:absolute;right:52px;top:310px;text-align:right;font-family:'Roboto',sans-serif;font-size:17px;color:var(--contact)}
  .contact__row{display:flex;align-items:center;justify-content:flex-end;gap:8px;height:26px}
  .contact__row svg{width:16px;height:16px;fill:var(--contact)}
  .band-line{position:absolute;left:0;right:0;top:385px;height:3px;background:var(--gold)}
  .band{position:absolute;left:0;right:0;top:392px;bottom:0;
    background:linear-gradient(100deg,var(--gold-deep) 0%,var(--gold-light) 35%,var(--gold) 60%,#fff06a 100%);
    display:flex;align-items:center;justify-content:center;
    font-family:'Montserrat',sans-serif;font-weight:700;font-size:15px;letter-spacing:1px;color:var(--band-text)}
</style>
</head>
<body>
<main class="canvas">
  <section class="card card--front">
    <div class="brand">
      <span class="brand__mark"></span>
      <div class="brand__name">VORNEL TRUCK &amp; EQUIPMENT</div>
      <div class="brand__sub">FINANCING</div>
    </div>
    <div class="divider"></div>
    <div class="person">
      <div class="person__name">DEREK MOWAT</div>
      <div class="person__title">PRESIDENT</div>
    </div>
    <div class="contact">
      <div class="contact__row">403 555 0172
        <svg viewBox="0 0 24 24" aria-hidden="true"><path d="M6.6 10.8a15 15 0 0 0 6.6 6.6l2.2-2.2c.3-.3.7-.4 1-.2 1.1.4 2.3.6 3.6.6.6 0 1 .4 1 1V20c0 .6-.4 1-1 1C10.6 21 3 13.4 3 4c0-.6.4-1 1-1h3.5c.6 0 1 .4 1 1 0 1.3.2 2.5.6 3.6.1.3 0 .7-.2 1z"/></svg>
      </div>
      <div class="contact__row">Derek.Vornelli@quillbrookfunding.com
        <svg viewBox="0 0 24 24" aria-hidden="true"><path d="M2 5h20v14H2zm2 2v.5l8 5 8-5V7l-8 5z"/></svg>
      </div>
    </div>
    <div class="band-line"></div>
    <div class="band">EQUIPMENT FINANCE SPECIALIST</div>
  </section>

  <section class="card card--back">
    <div class="brand">
      <span class="brand__mark"></span>
      <div class="brand__name">VORNEL TRUCK &amp; EQUIPMENT</div>
      <div class="brand__sub">FINANCING</div>
    </div>
  </section>
</main>
</body>
</html>
```